Orthodontic Office Needs New Stationary

We have recently renovated our office and are opening a second location. We need new stationary/branding to go with our new look. We like our logo, but are open to changing the colors to match the office look/feel more.

```html
<!DOCTYPE html>
<html lang="en">
<head>
<meta charset="utf-8">
<title>Halden &amp; Moro Orthodontics — Stationery</title>
<link href="https://fonts.googleapis.com/css2?family=Montserrat:wght@300;400;500&family=Arimo:wght@400;700&display=swap" rel="stylesheet">
<style>
:root{
  --backdrop:#a9a9a9;
  --orange:#f89c27;
  --paper:#ffffff;
  --paper-shade:#e6e6e6;
  --ink:#3a3a3a;
  --ink-soft:#8a8a8a;
  --rule:#5a5a5a;
  --shadow:2px 2px 3px rgba(0,0,0,.35);
}
*{margin:0;padding:0;box-sizing:border-box}
html,body{width:998px;height:1200px;overflow:hidden;background:var(--backdrop)}
body{position:relative;font-family:"Montserrat",sans-serif;color:var(--ink)}
.item{position:absolute;box-shadow:var(--shadow);overflow:hidden}
.paper{background:linear-gradient(90deg,var(--paper-shade) 0%,var(--paper) 55%)}

/* brand name: one colour, one weight */
.brand{font-family:"Montserrat",sans-serif;font-weight:400;color:var(--orange);line-height:1;white-space:nowrap}
.brand .name{display:block;letter-spacing:.02em}
.brand .line2{display:block;letter-spacing:.4em}
.brand.on-orange{color:#fff}

/* contact */
.contact{font-family:"Arimo",sans-serif;color:var(--ink);line-height:1.3}
.contact li{list-style:none;display:flex;align-items:center;gap:4px}
.contact svg{flex:none}
.contact .hl{color:var(--orange)}

/* business card */
.card-front{left:151px;top:38px;width:337px;height:193px}
.card-front .brand{position:absolute;left:21px;top:86px}
.card-front .brand .name{font-size:14.5px}
.card-front .brand .line2{font-size:10px;margin-top:1px}
.card-front .divider{position:absolute;left:168px;top:49px;width:1px;height:93px;background:var(--rule)}
.card-front .person{position:absolute;left:180px;top:47px;font-family:"Arimo",sans-serif}
.person .full-name{color:var(--orange);font-weight:700;font-size:11.5px}
.person .role{font-size:9.5px;margin-top:1px}
.card-front .address{font-size:9.5px;margin-top:10px;line-height:1.2}
.card-front .contact{font-size:9.5px;margin-top:9px;line-height:1.22}
.card-back{left:519px;top:38px;width:337px;height:193px;background:var(--orange)}
.card-back .brand{position:absolute;left:72px;top:80px}
.card-back .brand .name{font-size:21px}
.card-back .brand .line2{font-size:13.5px;margin-top:1px}

/* letterhead */
.letterhead{left:43px;top:264px;width:445px;height:629px}
.letterhead .brand{position:absolute;left:29px;top:38px}
.letterhead .brand .name{font-size:11.4px}
.letterhead .brand .line2{font-size:7.8px}
.letterhead .contact-block{position:absolute;left:336px;top:18px;font-family:"Arimo",sans-serif;font-size:6.5px}
.letterhead .contact-block .contact{margin-top:5px;font-size:6.5px}
.letterhead .head-rule{position:absolute;left:29px;top:71px;width:387px;height:1px;background:var(--rule)}
.recipient{position:absolute;left:45px;top:140px;font-size:6px;color:var(--ink-soft);line-height:1.65}
.recipient .to{font-size:8px;letter-spacing:.12em;color:var(--ink)}
.recipient .r-name{font-size:7px;color:var(--orange)}
.letterhead .date{position:absolute;left:345px;top:141px;font-size:6px;color:var(--ink-soft)}
.letter-body{position:absolute;left:45px;top:225px;width:355px;font-size:5.5px;font-weight:300;color:#777;line-height:1.45;text-align:justify}
.letter-body p{margin-bottom:7px}
.signature{position:absolute;left:45px;top:443px;width:76px;height:18px;background:linear-gradient(90deg,#e8e8e8,#f4f4f4)}
.signer{position:absolute;left:44px;top:469px;font-size:7px}
.signer .title{font-size:5.5px;color:var(--ink-soft)}

/* folder closed */
.folder{left:519px;top:264px;width:426px;height:301px;background:var(--orange)}
.folder .spine-mark{position:absolute;left:0;top:0;height:301px;writing-mode:vertical-rl;transform:rotate(180deg);color:rgba(255,255,255,.3);line-height:.95}
.folder .spine-mark .name{font-size:36px;letter-spacing:.01em}
.folder .spine-mark .line2{font-size:23px;letter-spacing:.3em}
.folder .cover{position:absolute;left:213px;top:0;width:213px;height:301px}
.folder .cover .brand{position:absolute;left:47px;top:12px}
.folder .cover .brand .name{font-size:13px}
.folder .cover .brand .line2{font-size:8.8px}
.mini-foot{position:absolute;left:77px;top:282px;display:flex;gap:3px;font-family:"Arimo",sans-serif;font-size:2.6px;line-height:1.4}
.mini-foot .addr{text-align:right;border-right:.5px solid var(--rule);padding-right:3px}

/* folder open */
.folder-open{left:519px;top:592px;width:426px;height:301px;background:#fff}
.folder-open .panel-left{position:absolute;left:0;top:0;width:213px;height:301px;background:linear-gradient(90deg,#fff 0%,#eee 85%,#dcdcdc 100%)}
.folder-open .panel-right{position:absolute;left:213px;top:0;width:213px;height:301px;background:linear-gradient(90deg,#d8d8d8,#f2f2f2 40%,#fff)}
.mini-sheet{position:absolute;left:224px;top:15px;width:193px;height:180px;background:linear-gradient(90deg,#f0f0f0,#fff 40%,#fafafa);font-size:2.4px;color:#888;line-height:1.4}
.mini-sheet .brand{position:absolute;left:12px;top:16px}
.mini-sheet .brand .name{font-size:5px}
.mini-sheet .brand .line2{font-size:3.3px}
.mini-sheet .m-contact{position:absolute;left:145px;top:8px;font-family:"Arimo",sans-serif;color:var(--ink)}
.mini-sheet .m-rule{position:absolute;left:12px;top:45px;width:172px;height:.5px;background:var(--rule)}
.mini-sheet .m-to{position:absolute;left:19px;top:74px}
.mini-sheet .m-date{position:absolute;left:149px;top:74px}
.mini-sheet .m-body{position:absolute;left:19px;top:112px;width:158px}
.mini-sheet .m-body p{margin-bottom:3px}
.pockets{position:absolute;left:0;top:0}

/* envelopes */
.envelope-back{left:33px;top:933px;width:455px;height:198px}
.envelope-back .brand{position:absolute;left:16px;top:17px}
.envelope-back .brand .name{font-size:8.7px}
.envelope-back .brand .line2{font-size:6px}
.envelope-back .address{position:absolute;left:16px;top:35px;font-family:"Arimo",sans-serif;font-size:6px;line-height:1.2}
.envelope-front{left:519px;top:933px;width:455px;height:198px;background:linear-gradient(90deg,#eee,#fff 45%)}
.envelope-front .flap{position:absolute;left:0;top:0}
.envelope-front .brand{position:absolute;left:155px;top:15px}
.envelope-front .brand .name{font-size:16px}
.envelope-front .brand .line2{font-size:11px;margin-top:1px}
</style>
</head>
<body>

<svg width="0" height="0" style="position:absolute" aria-hidden="true">
  <defs>
    <symbol id="icon-phone" viewBox="0 0 10 10"><path d="M2 1l2 2-1 1.2c.6 1.2 1.5 2.1 2.8 2.8L7 6l2 2-1.3 1.3C4.5 9 1 5.5.7 2.3z" fill="#f89c27"/></symbol>
    <symbol id="icon-mail" viewBox="0 0 10 10"><rect x="0.5" y="2" width="9" height="6" fill="#f89c27"/><path d="M.5 2l4.5 3.5L9.5 2" stroke="#fff" stroke-width=".8" fill="none"/></symbol>
    <symbol id="icon-web" viewBox="0 0 10 10"><circle cx="5" cy="5" r="4.5" fill="#f89c27"/><path d="M.5 5h9M5 .5c-2 2.5-2 6.5 0 9M5 .5c2 2.5 2 6.5 0 9" stroke="#fff" stroke-width=".6" fill="none"/></symbol>
  </defs>
</svg>

<!-- business card front -->
<section class="item paper card-front">
  <div class="brand"><span class="name">HALDEN &amp; MORO</span><span class="line2">ORTHODONTICS</span></div>
  <div class="divider"></div>
  <div class="person">
    <div class="full-name">DANIEL REYES</div>
    <div class="role">Manager</div>
    <div class="address">Your address, city<br>state, ZIP 0000</div>
    <ul class="contact">
      <li><svg width="7" height="7"><use href="#icon-phone"/></svg><span>123-456-2100</span></li>
      <li><svg width="7" height="7"><use href="#icon-mail"/></svg><span>youremail@mailbox.com</span></li>
      <li><svg width="7" height="7"><use href="#icon-web"/></svg><span>www.<span class="hl">yourwebsite</span>.com</span></li>
    </ul>
  </div>
</section>

<!-- business card back -->
<section class="item card-back">
  <div class="brand on-orange"><span class="name">HALDEN &amp; MORO</span><span class="line2">ORTHODONTICS</span></div>
</section>

<!-- letterhead -->
<section class="item paper letterhead">
  <div class="brand"><span class="name">HALDEN &amp; MORO</span><span class="line2">ORTHODONTICS</span></div>
  <div class="contact-block">
    <div>Your address, city<br>state, ZIP 0000</div>
    <ul class="contact">
      <li><svg width="5" height="5"><use href="#icon-phone"/></svg><span>123-456-2100</span></li>
      <li><svg width="5" height="5"><use href="#icon-mail"/></svg><span>youremail@mailbox.com</span></li>
      <li><svg width="5" height="5"><use href="#icon-web"/></svg><span>www.<span class="hl">yourwebsite</span>.com</span></li>
    </ul>
  </div>
  <div class="head-rule"></div>
  <div class="recipient">
    <div class="to">TO</div>
    <div class="r-name">Lena Harwick</div>
    <div>Human Resources</div>
    <div>Brightfield Inc.</div>
    <div>214 Alder Row, Kestrel</div>
    <div>K21 USA</div>
  </div>
  <div class="date">Friday, 01/01/2018</div>
  <div class="letter-body">
    <p>Lorem ipsum dolor sit amet, consectetuer adipiscing elit, sed diam nonummy nibh euismod tincidunt ut laoreet dolore magna aliquam erat volutpat. Ut wisi enim ad minim veniam, quis nostrud exerci tation ullamcorper suscipit lobortis nisl ut aliquip ex ea commodo consequat. Duis autem vel eum iriure dolor in hendrerit in vulputate velit esse molestie consequat, vel illum dolore eu feugiat nulla facilisis at vero eros et accumsan et iusto odio dignissim qui blandit praesent luptatum zzril delenit augue duis dolore te feugait nulla facilisi.</p>
    <p>Nam liber tempor cum soluta nobis eleifend option congue nihil imperdiet doming id quod mazim placerat facer possim assum. Typi non habent claritatem insitam;</p>
    <p>Est usus legentis in iis qui facit eorum claritatem.</p>
    <p>Investigationes demonstraverunt lectores legere me lius quod ii legunt saepius. Claritas est etiam processus dynamicus, qui sequitur mutationem consuetudium lectorum. Mirum est notare quam littera gothica, quam nunc putamus parum claram, anteposuerit litterarum formas humanitatis per seacula quarta decima et quinta decima. Eodem modo typi, qui nunc nobis videntur parum clari, fiant sollemnes in futurum.</p>
    <p>consectetuer adipiscing elit, sed diam nonummy nibh euismod tincidunt ut laoreet dolore magna aliquam erat volutpat. Ut wisi enim ad minim veniam, quis nostrud exerci tation ullamcorper suscipit lobortis nisl ut aliquip ex ea commodo consequat. Duis autem vel eum iriure dolor in hendrerit in vulputate velit esse molestie consequat, vel illum dolore eu feugiat nulla facilisis at vero eros et accumsan et iusto odio dignissim qui blandit praesent luptatum zzril delenit augue duis dolore te feugait nulla facilisi.</p>
    <p>Nam liber tempor cum soluta nobis eleifend option congue nihil imperdiet .</p>
  </div>
  <div class="signature" role="img" aria-label="Handwritten signature"></div>
  <div class="signer">Owen Tarrant<div class="title">Managing Director</div></div>
</section>

<!-- presentation folder, closed -->
<section class="item folder">
  <div class="spine-mark brand on-orange"><span class="name">HALDEN &amp; MORO</span><span class="line2">ORTHODONTICS</span></div>
  <div class="cover paper">
    <div class="brand"><span class="name">HALDEN &amp; MORO</span><span class="line2">ORTHODONTICS</span></div>
    <div class="mini-foot">
      <div class="addr">Your address, city<br>state, ZIP 0000</div>
      <div>123-456-2100<br>youremail@mailbox.com<br>www.<span style="color:var(--orange)">yourwebsite</span>.com</div>
    </div>
  </div>
</section>

<!-- presentation folder, open -->
<section class="item folder-open">
  <div class="panel-left"></div>
  <div class="panel-right"></div>
  <div class="mini-sheet">
    <div class="brand"><span class="name">HALDEN &amp; MORO</span><span class="line2">ORTHODONTICS</span></div>
    <div class="m-contact">Your address, city<br>state, ZIP 0000<br>123-456-2100<br>youremail@mailbox.com<br>www.yourwebsite.com</div>
    <div class="m-rule"></div>
    <div class="m-to">TO<br><span style="color:var(--orange)">Lena Harwick</span><br>Human Resources<br>Brightfield Inc.<br>214 Alder Row, Kestrel<br>K21 USA</div>
    <div class="m-date">Friday, 01/01/2018</div>
    <div class="m-body">
      <p>Thank you for choosing our practice. We look forward to caring for your smile.</p>
      <p>Our new office is open on weekdays.</p>
      <p>Please call us to book your next visit.</p>
    </div>
  </div>
  <svg class="pockets" width="426" height="301" viewBox="0 0 426 301" aria-hidden="true">
    <path d="M0 195H195Q200 195 201 200L213 301H0Z" fill="#f89c27"/>
    <path d="M426 195H231Q226 195 225 200L213 301H426Z" fill="#f89c27"/>
  </svg>
</section>

<!-- envelope back -->
<section class="item paper envelope-back">
  <div class="brand"><span class="name">HALDEN &amp; MORO</span><span class="line2">ORTHODONTICS</span></div>
  <div class="address">Your address, city<br>state, ZIP 0000</div>
</section>

<!-- envelope front -->
<section class="item envelope-front">
  <svg class="flap" width="455" height="60" viewBox="0 0 455 60" aria-hidden="true">
    <defs><filter id="flap-shadow" x="-5%" y="-20%" width="110%" height="160%"><feDropShadow dx="0" dy="2" stdDeviation="2" flood-opacity=".3"/></filter></defs>
    <path d="M3 0H453L440 40Q435 54 418 54H30Q14 54 10 40Z" fill="#fff" filter="url(#flap-shadow)"/>
  </svg>
  <div class="brand"><span class="name">HALDEN &amp; MORO</span><span class="line2">ORTHODONTICS</span></div>
</section>

</body>
</html>
```